Event flyer for Sunday night Youth Group

Need a 4 x 6 or 5 x 7 flyer for a new youth group starting on April 14. The youth group is for students in middle school and high school so it needs to look fun and cool, but not childish. I prefer it not to include pictures of people unless it's so obscure you can't really see their faces. I've uploaded some pictures of flyers I like. I've also attached a couple versions of our logo to use on the flyer.
Information the flyer needs to include:
Youth Group
Sundays, 6-8pm (beginning April 14)
Location: Merriwick's - 4219 Hollowfern Ln S, Keizer, 97418
There will be dinner, games, friends, and a message.
Target Market(s)
Youth ages 13-18
Industry/Entity Type
Church
Colors
Designer to choose colors to be used in the design.
Look and feel

```html
<!DOCTYPE html>
<html lang="en">
<head>
<meta charset="utf-8">
<title>Youth Group Flyer</title>
<link rel="stylesheet" href="https://fonts.googleapis.com/css2?family=Arimo:ital,wght@0,400;0,700;1,400&family=Montserrat:wght@600&display=swap">
<style>
  :root {
    --orange: #f7901e;
    --tangerine: #f46b1c;
    --pink: #e8336c;
    --magenta: #c41fae;
    --purple: #8a3fc4;
    --green: #4bb86b;
    --blue: #1aa3e8;
    --ink: #25424d;
    --white: #ffffff;
    --shadow-red: #c3202f;
    --shadow-orange: #f7941d;
  }
  * { margin: 0; padding: 0; box-sizing: border-box; }
  html, body { width: 857px; height: 1200px; overflow: hidden; background: #fff; }
  .flyer {
    position: relative;
    width: 857px;
    height: 1200px;
    overflow: hidden;
    font-family: "Arimo", Arial, sans-serif;
    color: var(--white);
    background:
      radial-gradient(ellipse 360px 300px at 700px 720px, rgba(75,184,107,0.95), transparent 70%),
      radial-gradient(ellipse 260px 320px at 840px 1060px, rgba(26,163,232,0.9), transparent 70%),
      radial-gradient(ellipse 320px 260px at 430px 1180px, rgba(138,63,196,0.9), transparent 70%),
      radial-gradient(ellipse 360px 300px at 760px 480px, rgba(196,31,174,0.95), transparent 70%),
      radial-gradient(ellipse 380px 320px at 500px 600px, rgba(232,51,108,0.95), transparent 70%),
      linear-gradient(100deg, var(--orange) 0%, var(--tangerine) 35%, var(--pink) 60%, var(--magenta) 100%);
  }
  .backdrop { position: absolute; inset: 0; width: 857px; height: 1200px; }

  .brand {
    position: absolute;
    left: 160px;
    top: 140px;
    display: flex;
    align-items: center;
    gap: 16px;
    white-space: nowrap;
  }
  .brand-mark { width: 36px; height: 36px; background: var(--ink); }
  .brand-name {
    font-family: "Montserrat", Arial, sans-serif;
    font-weight: 600;
    font-size: 38px;
    letter-spacing: 1px;
    color: var(--ink);
    text-transform: uppercase;
  }

  .photo-hands {
    position: absolute;
    left: -20px;
    top: 560px;
    width: 500px;
    height: 580px;
    background:
      radial-gradient(ellipse 200px 230px at 250px 290px, rgba(240,214,200,0.95), transparent 75%),
      radial-gradient(ellipse 260px 290px at 250px 290px, rgba(226,190,168,0.7), transparent 80%);
    filter: blur(6px);
  }

  .headline {
    position: absolute;
    font-weight: 400;
    line-height: 1;
    letter-spacing: -4px;
    color: var(--white);
    text-shadow: 3px 3px 0 var(--shadow-orange), 5px 5px 0 var(--shadow-red);
  }
  .headline-youth { left: 62px; top: 348px; font-size: 188px; }
  .headline-group { left: 292px; top: 497px; font-size: 139px; }

  .details { position: absolute; left: 472px; top: 689px; width: 375px; }
  .details-rule { height: 2px; background: var(--white); }
  .details-block { padding: 18px 0 20px; }
  .details-when { font-weight: 700; font-size: 30px; line-height: 1.1; }
  .details-start { font-size: 28px; line-height: 1.15; }
  .details-label { font-size: 26px; line-height: 1.1; }
  .details-venue { font-weight: 700; font-size: 50px; line-height: 1.05; }
  .details-address { font-size: 23px; line-height: 1.05; }

  .tagline {
    position: absolute;
    left: 70px;
    top: 1134px;
    font-style: italic;
    font-size: 31px;
    letter-spacing: -0.3px;
    white-space: nowrap;
  }
</style>
</head>
<body>
<main class="flyer">
  <svg class="backdrop" viewBox="0 0 857 1200" aria-hidden="true">
    <defs>
      <linearGradient id="sky" x1="0" y1="0" x2="1" y2="0.4">
        <stop offset="0" stop-color="#f9e7a0"/>
        <stop offset="0.45" stop-color="#f4c7b0"/>
        <stop offset="0.75" stop-color="#eab6d8"/>
        <stop offset="1" stop-color="#afe3d6"/>
      </linearGradient>
    </defs>
    <path class="sky" fill="url(#sky)" d="M0,0 H857 V340 C620,330 300,300 0,230 Z"/>
  </svg>

  <div class="brand">
    <span class="brand-mark"></span>
    <span class="brand-name">Brightpath Fellowship</span>
  </div>

  <div class="photo-hands" role="img" aria-label="Photo of four hands clasping each other's wrists in a square, seen from above"></div>

  <h1>
    <span class="headline headline-youth">YOUTH</span>
    <span class="headline headline-group">GROUP</span>
  </h1>

  <section class="details">
    <div class="details-rule"></div>
    <div class="details-block">
      <p class="details-when">Sundays, 6-8pm</p>
      <p class="details-start">(beginning April 14)</p>
    </div>
    <div class="details-rule"></div>
    <div class="details-block">
      <p class="details-label">Location:</p>
      <p class="details-venue">Merriwick's</p>
      <p class="details-address">4219 Hollowfern Ln.<br>S, Keizer, 97418</p>
    </div>
    <div class="details-rule"></div>
  </section>

  <p class="tagline">There will be dinner, games, friends, and a message.</p>
</main>
</body>
</html>
```